Create a pouch design for a new sports supplement product

Dimensions are 235mm (width) x 335mm (length) x 110mm (gusset)
File 1 - Extension of design brief please read both briefs
File 2 - Is 2 potential pouches this is just to give you a better example of size the dimensions are for the pouch on the right. This picture is not to give you design ideas as I am not very keen on either of these designs.
We need a design to be printed onto the pouches of our whey protein product. The brand name is 'Brisk Fuelworks' and needs to be displayed on the packaging either just writing or a simple logo design. I am not the most creative person in the world but have put together a more detailed brief listing some of the key information that needs to be included on the pouch (See attachment) Please feel free if you have experience of this the sports supplement market or have different ideas then please feel free to explore them.
The pouch would either be printed straight onto the pouch, or possibly just a printed label (front & back) to be stuck onto the pouch. Please design either or both.
Open to different colour schemes. Design has to be modern looking and eye-catching.
Some key points;
High quality whey protein concentrate
All Natural
Soy free
Great tasting
Please google image search 'protein pouches' to see other designs if your not familiar with the sports supplement market.
Any questions feel free to ask.
Updates
Project Deadline Extended
Reason: give me chance to give feedback
Hi, Thanks for all your design! I am really busy at the moment so haven't had chance to give feedback and have a proper look through all the designs. I have extended the time frame to give myself chance to give proper feedback and see any changes needed. Expect feedback sunday at the latest, and I will be pick a design early next week.
Target Market(s)
Sports supplement market. Product is a whey protein shake
Industry/Entity Type
Nutrition
Look and feel
Each slider illustrates characteristics of the customer's brand and the style your logo design should communicate.

```html
<!DOCTYPE html>
<html lang="en">
<head>
<meta charset="utf-8">
<title>Brisk Fuelworks – Natural Whey Protein Pouch</title>
<link rel="stylesheet" href="https://fonts.googleapis.com/css2?family=Teko:wght@600&family=Roboto+Condensed:wght@300;400&display=swap">
<style>
  :root {
    --brand-red: #d03a30;
    --fold-red: #9c241d;
    --claim-yellow: #e2d400;
    --paper: #ffffff;
    --droplet-tint: #e9e9e9;
  }
  * { margin: 0; padding: 0; box-sizing: border-box; }
  html, body { width: 842px; height: 1200px; overflow: hidden; background: var(--paper); }
  .pouch-front {
    position: relative;
    width: 842px;
    height: 1200px;
    overflow: hidden;
    background: var(--paper);
    font-family: "Roboto Condensed", sans-serif;
  }
  .droplet-texture {
    position: absolute;
    inset: 0;
    background: radial-gradient(ellipse at 50% 45%, var(--paper) 0%, #f6f6f6 55%, var(--droplet-tint) 100%);
  }
  .reseal-band {
    position: absolute;
    left: 0; top: 47px;
    width: 842px; height: 39px;
    background: var(--brand-red);
  }
  .reseal-label {
    position: absolute;
    right: 34px; top: 0;
    line-height: 39px;
    color: var(--paper);
    font-family: "Roboto Condensed", sans-serif;
    font-weight: 400;
    font-size: 30px;
    letter-spacing: 0.2px;
  }
  .brand-title {
    position: absolute;
    left: 0; top: 0;
    width: 842px; height: 800px;
  }
  .brand-title text {
    font-family: "Teko", sans-serif;
    font-weight: 600;
    fill: var(--brand-red);
  }
  .product-ribbon {
    position: absolute;
    left: 141px; top: 681px;
    width: 701px; height: 76px;
    background: var(--brand-red);
  }
  .ribbon-tail {
    position: absolute;
    left: 0; top: 719px;
    width: 182px; height: 75px;
    background: var(--brand-red);
  }
  .ribbon-fold {
    position: absolute;
    left: 0; top: 0;
    width: 842px; height: 800px;
  }
  .product-name {
    position: absolute;
    left: 180px; top: 681px;
    width: 520px;
    line-height: 76px;
    color: var(--claim-yellow);
    font-family: "Teko", sans-serif;
    font-weight: 600;
    font-size: 58px;
    letter-spacing: -0.5px;
    white-space: nowrap;
  }
  .benefit-list {
    position: absolute;
    right: 32px; top: 790px;
    list-style: none;
    text-align: right;
    color: var(--brand-red);
    font-family: "Roboto Condensed", sans-serif;
    font-weight: 400;
    font-size: 29px;
    line-height: 40.5px;
    letter-spacing: -0.6px;
  }
  .flavour-fruit {
    position: absolute;
    left: 68px; top: 1010px;
    width: 152px; height: 148px;
    border-radius: 48% 52% 50% 50% / 40% 40% 60% 60%;
    background: radial-gradient(circle at 40% 40%, #f0473c 0%, #d8261e 60%, #a8150f 100%);
  }
  .flavour-name {
    position: absolute;
    left: 226px; top: 1063px;
    width: 140px;
    text-align: center;
    color: var(--brand-red);
    font-family: "Roboto Condensed", sans-serif;
    font-weight: 300;
    font-size: 23px;
    line-height: 24px;
  }
  .base-band {
    position: absolute;
    left: 0; top: 1136px;
    width: 842px; height: 64px;
    background: var(--brand-red);
  }
</style>
</head>
<body>
<main class="pouch-front">
  <div class="droplet-texture" role="img" aria-label="Water droplets scattered across a white background"></div>

  <div class="reseal-band">
    <span class="reseal-label">Tear here &amp; Reseal</span>
  </div>

  <svg class="brand-title" viewBox="0 0 842 800" aria-label="Brisk Fuelworks">
    <text x="141" y="523" font-size="290" textLength="570" lengthAdjust="spacingAndGlyphs">BRISK</text>
    <text x="141" y="673" font-size="170" textLength="570" lengthAdjust="spacingAndGlyphs">FUELWORKS</text>
  </svg>

  <div class="ribbon-tail"></div>
  <div class="product-ribbon"></div>
  <svg class="ribbon-fold" viewBox="0 0 842 800" aria-hidden="true">
    <polygon points="141,757 182,757 182,794" fill="var(--fold-red)"/>
  </svg>
  <p class="product-name">NATURAL WHEY PROTEIN</p>

  <ul class="benefit-list">
    <li>No artificial Flavours</li>
    <li>Excellent Amino acid profile</li>
    <li>80% high quality protein content</li>
    <li>Soy free</li>
  </ul>

  <div class="flavour-fruit" role="img" aria-label="Illustration of a ripe strawberry with green leaves"></div>
  <p class="flavour-name">Strawberry<br>flavour</p>

  <div class="base-band"></div>
</main>
</body>
</html>
```